New career and executive coaching business needs a business card design including logo

Company name: 'Harborline Growth Partners.' The aim of my coaching engagements is to help people improve their communication in the workplace and achieve their career goals. The process involves working with individuals to help them uncover their strengths and talents, then leverage those to improve their working lives. The Tavelle Inventory is the starting point to the process. I am after an exciting and interesting business card design (including logo)which is professional yet will still get people's attention.

Industry/Entity Type

Business

Contact Information for Business Card

Name: Gordon Halvey
Position: Owner
Address: 58 Merrowind Cres, Alderbrook Vic 3187
Phone: 0481936045
Website: harborlinegrowth.com.au
Email: gordon@hgp.com.au

Colors
33a6d7
00a990
0355a3
3176b5

Requirements
Must have
• logo

```html
<!DOCTYPE html>
<html lang="en">
<head>
<meta charset="utf-8">
<title>Harborline Growth Partners – Business Card</title>
<link rel="stylesheet" href="https://fonts.googleapis.com/css2?family=Roboto+Condensed:wght@300;700&family=Roboto:wght@400&display=swap">
<style>
  :root {
    --stage: #e4e6e8;
    --card-cream: #f1eee6;
    --brand-blue: #1b7eae;
    --ink-grey: #4a4a4a;
    --soft-grey: #c9c7c1;
    --pale-grey: #dedbd3;
    --white: #ffffff;
  }
  html, body {
    margin: 0;
    padding: 0;
    width: 1200px;
    height: 786px;
    overflow: hidden;
    background: var(--stage);
  }
  .stage {
    position: relative;
    width: 1200px;
    height: 786px;
    display: flex;
    align-items: center;
    justify-content: center;
    gap: 40px;
  }
  .card {
    position: relative;
    width: 540px;
    height: 310px;
    border-radius: 16px;
    overflow: hidden;
    box-shadow: 0 6px 18px rgba(0,0,0,0.18);
  }
  .card--front { background: var(--card-cream); }
  .card--back {
    background: var(--brand-blue);
    display: flex;
    align-items: center;
    justify-content: center;
  }
  .swoosh {
    position: absolute;
    left: 0;
    bottom: 0;
    width: 540px;
    height: 310px;
  }
  .holder {
    position: absolute;
    left: 210px;
    top: 34px;
    font-family: "Roboto Condensed", sans-serif;
  }
  .holder__name {
    margin: 0;
    font-weight: 700;
    font-size: 20px;
    letter-spacing: 0.5px;
    color: var(--brand-blue);
    text-transform: uppercase;
  }
  .holder__role {
    margin: 2px 0 0;
    font-weight: 300;
    font-size: 14px;
    color: var(--ink-grey);
  }
  .contact {
    position: absolute;
    left: 30px;
    top: 96px;
    margin: 0;
    padding: 0;
    list-style: none;
    font-family: "Roboto", sans-serif;
    font-size: 12.5px;
    color: var(--ink-grey);
    line-height: 21px;
  }
  .contact__item { display: flex; align-items: center; gap: 8px; }
  .contact__icon { width: 14px; height: 14px; flex: none; }
  .contact__address { margin-top: 8px; line-height: 18px; }
  .wordmark {
    font-family: "Roboto Condensed", sans-serif;
    font-weight: 700;
    text-transform: uppercase;
    display: flex;
    align-items: center;
    gap: 12px;
  }
  .wordmark__dot {
    width: 22px;
    height: 22px;
    border-radius: 50%;
    flex: none;
  }
  .wordmark__text { line-height: 1; }
  .wordmark__main { display: block; font-size: 38px; letter-spacing: 1px; }
  .wordmark__sub { display: block; font-size: 15px; letter-spacing: 2.6px; margin-top: 4px; }
  .card--front .wordmark {
    position: absolute;
    right: 30px;
    top: 150px;
    color: var(--brand-blue);
  }
  .card--front .wordmark__dot { background: var(--brand-blue); }
  .card--back .wordmark { color: var(--white); }
  .card--back .wordmark__dot { background: var(--white); }
  .card--back .wordmark__main { font-size: 44px; }
  .card--back .wordmark__sub { font-size: 17px; letter-spacing: 3px; }
</style>
</head>
<body>
<main class="stage">

  <section class="card card--front" aria-label="Business card front">
    <svg class="swoosh" viewBox="0 0 540 310" aria-hidden="true">
      <path d="M0 200 C120 250 260 260 340 310 L0 310 Z" fill="var(--pale-grey)"/>
      <path d="M0 222 C130 262 250 275 310 310 L0 310 Z" fill="var(--soft-grey)"/>
      <path d="M0 240 C140 272 230 288 270 310 L0 310 Z" fill="var(--brand-blue)"/>
    </svg>

    <div class="holder">
      <p class="holder__name">Gordon Halvey</p>
      <p class="holder__role">Owner</p>
    </div>

    <ul class="contact">
      <li class="contact__item">
        <svg class="contact__icon" viewBox="0 0 14 14" aria-hidden="true"><rect width="14" height="14" rx="3" fill="var(--brand-blue)"/><path d="M4 3.5 L5.6 3.5 L6.2 5.6 L5.2 6.3 C5.7 7.4 6.6 8.3 7.7 8.8 L8.4 7.8 L10.5 8.4 L10.5 10 C7 10 4 7 4 3.5 Z" fill="var(--white)"/></svg>
        <span>0481936045</span>
      </li>
      <li class="contact__item">
        <svg class="contact__icon" viewBox="0 0 14 14" aria-hidden="true"><rect width="14" height="14" rx="3" fill="var(--brand-blue)"/><rect x="3" y="4.2" width="8" height="5.6" fill="none" stroke="var(--white)" stroke-width="1"/><path d="M3 4.2 L7 7.4 L11 4.2" fill="none" stroke="var(--white)" stroke-width="1"/></svg>
        <span>gordon@hgp.com.au</span>
      </li>
      <li class="contact__item">
        <svg class="contact__icon" viewBox="0 0 14 14" aria-hidden="true"><rect width="14" height="14" rx="3" fill="var(--brand-blue)"/><circle cx="7" cy="7" r="3.8" fill="none" stroke="var(--white)" stroke-width="1"/><path d="M3.2 7 H10.8 M7 3.2 C5.4 5 5.4 9 7 10.8 M7 3.2 C8.6 5 8.6 9 7 10.8" fill="none" stroke="var(--white)" stroke-width="0.8"/></svg>
        <span>www.harborlinegrowth.com.au</span>
      </li>
      <li class="contact__address">58 Merrowind Cres<br>Alderbrook Vic 3187</li>
    </ul>

    <div class="wordmark">
      <span class="wordmark__dot"></span>
      <span class="wordmark__text">
        <span class="wordmark__main">Harborline</span>
        <span class="wordmark__sub">Growth Partners</span>
      </span>
    </div>
  </section>

  <section class="card card--back" aria-label="Business card back">
    <div class="wordmark">
      <span class="wordmark__dot"></span>
      <span class="wordmark__text">
        <span class="wordmark__main">Harborline</span>
        <span class="wordmark__sub">Growth Partners</span>
      </span>
    </div>
  </section>

</main>
</body>
</html>
```